New Business Card Design Project

Bloom of the Willow Wellness Clinic PLLC
Bloomofthewillowwc-example.com
Board Certified Nursing Coach in life, health, & wellness.
Hypnotherapy, weight loss & vitamin supplement injections, IV hydration.
Offering mobile clinics

```html
<!DOCTYPE html>
<html lang="en">
<head>
<meta charset="utf-8">
<title>Bloom of the Willow Wellness Clinic PLLC — Business Card</title>
<link href="https://fonts.googleapis.com/css2?family=Arimo:wght@400;700&display=swap" rel="stylesheet">
<style>
  :root {
    --stage: #1c1c1e;
    --card: #54302f;
    --accent: #f26a1b;
    --accent-soft: #f7a23a;
    --ink: #ffffff;
    --muted: #b9a8a6;
    --divider: #8a6a67;
  }
  * { box-sizing: border-box; margin: 0; padding: 0; }
  html, body {
    width: 1200px; height: 874px; overflow: hidden;
    background: var(--stage);
    font-family: "Arimo", Arial, sans-serif;
  }
  .stage {
    width: 1200px; height: 874px;
    display: flex; flex-direction: column; align-items: center; justify-content: center;
    gap: 30px;
  }
  .card {
    position: relative;
    width: 700px; height: 400px;
    background: var(--card);
    border-radius: 26px;
    overflow: hidden;
  }
  /* Front */
  .card--front { display: flex; flex-direction: column; align-items: center; }
  .emblem {
    margin-top: 54px;
    width: 210px; height: 210px; border-radius: 50%;
    background: radial-gradient(circle at 50% 40%, #fde3b4 0%, var(--accent-soft) 35%, var(--accent) 65%, rgba(84,48,47,0) 72%);
  }
  .front-name {
    margin-top: 12px;
    color: var(--accent-soft);
    font-size: 20px; letter-spacing: 2px;
  }
  .tagline {
    margin-top: 18px;
    color: var(--muted);
    font-size: 16px; line-height: 1.3; text-align: center;
  }
  /* Back */
  .card--back { display: flex; align-items: center; }
  .brand {
    width: 340px; padding-left: 50px;
    display: flex; align-items: center; gap: 14px;
  }
  .brand-dot {
    flex: none; width: 46px; height: 46px; border-radius: 50%;
    background: var(--accent);
  }
  .brand-name {
    color: var(--ink);
    font-size: 18px; letter-spacing: 2px; line-height: 1.35;
    text-transform: uppercase;
  }
  .divider {
    width: 2px; height: 220px;
    background: linear-gradient(to bottom, rgba(138,106,103,0), var(--divider), rgba(138,106,103,0));
  }
  .contact { padding-left: 22px; color: var(--ink); }
  .person-name { color: var(--accent); font-size: 30px; font-weight: 700; }
  .person-role { font-size: 17px; margin-bottom: 16px; }
  .address { font-size: 17px; line-height: 1.3; margin-bottom: 12px; }
  .contact-list { list-style: none; font-size: 16px; line-height: 1.35; }
  .contact-list li { display: flex; align-items: center; gap: 10px; }
  .contact-list svg { width: 14px; height: 14px; flex: none; }
</style>
</head>
<body>
<main class="stage">
  <section class="card card--front">
    <div class="emblem" role="img" aria-label="Clinic emblem area"></div>
    <p class="front-name">BLOOM OF THE WILLOW</p>
    <p class="tagline">Hypnotherapy, weight loss &amp; vitamin supplement injections<br>IV hydration. Offering mobile clinics</p>
  </section>

  <section class="card card--back">
    <div class="brand">
      <span class="brand-dot"></span>
      <p class="brand-name">Bloom of the Willow<br>Wellness Clinic</p>
    </div>
    <div class="divider"></div>
    <div class="contact">
      <p class="person-name">Daniel Reyes</p>
      <p class="person-role">President</p>
      <p class="address">1420 Cedar Hollow Road<br>Fairbrook, Canada 58210</p>
      <ul class="contact-list">
        <li><svg viewBox="0 0 16 16"><path fill="#f26a1b" d="M3 1l3 3-2 2c1 2 3 4 5 5l2-2 3 3-2 3C6 14 2 10 1 3z"/></svg>555-218-4470</li>
        <li><svg viewBox="0 0 16 16"><rect x="4" y="1" width="8" height="14" rx="1.5" fill="none" stroke="#f26a1b" stroke-width="2"/></svg>555-390-6126</li>
        <li><svg viewBox="0 0 16 16"><rect x="1" y="3" width="14" height="10" fill="#f26a1b"/><path d="M1 3l7 6 7-6" fill="none" stroke="#54302f" stroke-width="1.5"/></svg>info@bloomofthewillowwc-example.com</li>
        <li><svg viewBox="0 0 16 16"><circle cx="8" cy="8" r="7" fill="#f26a1b"/><path d="M1 8h14M8 1c-3 4-3 10 0 14M8 1c3 4 3 10 0 14" fill="none" stroke="#54302f" stroke-width="1.2"/></svg>www.bloomofthewillowwc-example.com</li>
      </ul>
    </div>
  </section>
</main>
</body>
</html>
```